Marlowbeck Media Stationary

Start up company requires matching stationary templates for Business Cards, letterhead and 'With Compliments' slips. The final design should keep with the style of our kiosk design, investor brochure and other collateral.

```html
<!DOCTYPE html>
<html lang="en">
<head>
<meta charset="utf-8">
<title>Marlowbeck Media – Letterhead</title>
<link href="https://fonts.googleapis.com/css2?family=Questrial&display=swap" rel="stylesheet">
<style>
  :root {
    --backdrop: #e6e6e6;
    --paper: #f6f6f6;
    --brand-blue: #4a77c4;
    --ink-grey: #6f6f6f;
    --rule-grey: #c4c4c4;
    --ornament-tone: #ececec;
  }
  * { box-sizing: border-box; margin: 0; padding: 0; }
  html, body {
    width: 1200px;
    height: 936px;
    overflow: hidden;
    background: var(--backdrop);
    font-family: "Questrial", "Century Gothic", sans-serif;
  }
  .letterhead {
    position: absolute;
    left: 290px;
    top: 30px;
    width: 620px;
    height: 876px;
    background: var(--paper);
    box-shadow: 0 2px 10px rgba(0,0,0,0.08);
  }
  .film-ornament {
    position: absolute;
    left: 250px;
    top: 0;
    width: 170px;
    height: 118px;
    border-radius: 0 0 60px 60px;
    background: linear-gradient(160deg, var(--ornament-tone), var(--paper));
  }
  .brand {
    position: absolute;
    left: 48px;
    top: 92px;
    display: flex;
    align-items: center;
    gap: 10px;
  }
  .brand-square {
    width: 26px;
    height: 26px;
    border-radius: 4px;
    background: var(--brand-blue);
  }
  .brand-name {
    font-size: 24px;
    color: var(--brand-blue);
    letter-spacing: 0.5px;
  }
  .contact-footer {
    position: absolute;
    left: 48px;
    right: 40px;
    bottom: 34px;
    display: flex;
    align-items: flex-start;
    font-size: 8.5px;
    line-height: 1.6;
    color: var(--ink-grey);
  }
  .office {
    padding: 0 12px;
    border-left: 1px solid var(--rule-grey);
  }
  .office:first-child { padding-left: 0; border-left: none; }
  .office-label {
    color: var(--brand-blue);
    text-transform: uppercase;
    letter-spacing: 0.3px;
  }
  .contact-line {
    display: flex;
    align-items: center;
    gap: 5px;
    white-space: nowrap;
  }
  .contact-icon { width: 10px; height: 10px; flex: none; }
</style>
</head>
<body>
  <main class="letterhead">
    <div class="film-ornament" role="img" aria-label="Faint film strip decoration curling down from the top edge"></div>

    <header class="brand">
      <span class="brand-square"></span>
      <span class="brand-name">Marlowbeck Media</span>
    </header>

    <footer class="contact-footer">
      <div class="office">
        <div class="contact-line"><span class="office-label">Sydney Office:</span> 18/52 Harbour Lane,</div>
        <div class="contact-line">Sydney NSW 2000
          <svg class="contact-icon" viewBox="0 0 10 10"><rect width="10" height="10" rx="1.5" fill="#4a77c4"/><path d="M3 2.2 L4.2 2.2 L4.6 3.8 L3.9 4.4 Q4.6 5.6 5.6 6.1 L6.2 5.4 L7.8 5.8 L7.8 7 Q5.8 7.6 3.9 5.8 Q2.4 4.2 3 2.2Z" fill="#fff"/></svg>
          (07) 555 0142</div>
      </div>
      <div class="office">
        <div class="office-label">Brisbane Office:</div>
        <div class="contact-line">
          <svg class="contact-icon" viewBox="0 0 10 10"><rect width="10" height="10" rx="1.5" fill="#4a77c4"/><path d="M3 2.2 L4.2 2.2 L4.6 3.8 L3.9 4.4 Q4.6 5.6 5.6 6.1 L6.2 5.4 L7.8 5.8 L7.8 7 Q5.8 7.6 3.9 5.8 Q2.4 4.2 3 2.2Z" fill="#fff"/></svg>
          (07) 555 0142</div>
      </div>
      <div class="office">
        <div class="office-label">Melbourne Office:</div>
        <div class="contact-line">
          <svg class="contact-icon" viewBox="0 0 10 10"><rect width="10" height="10" rx="1.5" fill="#4a77c4"/><path d="M3 2.2 L4.2 2.2 L4.6 3.8 L3.9 4.4 Q4.6 5.6 5.6 6.1 L6.2 5.4 L7.8 5.8 L7.8 7 Q5.8 7.6 3.9 5.8 Q2.4 4.2 3 2.2Z" fill="#fff"/></svg>
          (03) 555 0178</div>
      </div>
      <div class="office">
        <div class="contact-line">
          <svg class="contact-icon" viewBox="0 0 10 10"><rect width="10" height="10" rx="1.5" fill="#4a77c4"/><circle cx="5" cy="5" r="3" fill="none" stroke="#fff" stroke-width="0.8"/><path d="M2 5 H8 M5 2 Q3.5 5 5 8 M5 2 Q6.5 5 5 8" fill="none" stroke="#fff" stroke-width="0.7"/></svg>
          www.marlowbeckmedia.com.au</div>
        <div class="contact-line">
          <svg class="contact-icon" viewBox="0 0 10 10"><rect width="10" height="10" rx="1.5" fill="#4a77c4"/><rect x="2" y="3" width="6" height="4.2" fill="none" stroke="#fff" stroke-width="0.8"/><path d="M2 3 L5 5.4 L8 3" fill="none" stroke="#fff" stroke-width="0.8"/></svg>
          hello@marlowbeckmedia.com.au</div>
      </div>
    </footer>
  </main>
</body>
</html>
```